Silver Heron Holdings, LLC Business Card

We need a logo that will be embossed or printed in a singular light color for Business Cards. Would be interested in seeing a Cypress Tree graphic. Our company name is Silver Heron Holdings, LLC. Business Card layout and graphic should project imagine of confidence, integrity and strength.

```html
<!DOCTYPE html>
<html lang="en">
<head>
<meta charset="UTF-8">
<title>Silver Heron Holdings, LLC – Business Card</title>
<link rel="stylesheet" href="https://fonts.googleapis.com/css2?family=Cinzel:wght@400;500&family=Lato:wght@400&display=swap">
<style>
  :root {
    --page-bg: #e6ddc4;
    --card-white: #ffffff;
    --card-black: #050505;
    --ink: #111111;
    --text-grey: #333333;
    --emblem-grey: #b3b3b3;
    --tagline: #f2f2f2;
  }
  * { box-sizing: border-box; margin: 0; padding: 0; }
  html, body {
    width: 1200px; height: 800px; overflow: hidden;
    background: var(--page-bg);
  }
  .canvas {
    width: 1200px; height: 800px;
    display: flex; align-items: center; justify-content: center; gap: 40px;
  }
  .card {
    position: relative;
    width: 540px; height: 310px;
    border-radius: 40px;
    overflow: hidden;
    box-shadow: 0 6px 18px rgba(0,0,0,0.18);
  }
  /* Front */
  .card-front { background: var(--card-white); }
  .company-name {
    position: absolute; top: 30px; left: 40px; right: 30px;
    font-family: "Cinzel", serif; font-weight: 400;
    font-size: 31px; letter-spacing: 0.5px;
    color: var(--ink); text-align: right; white-space: nowrap;
  }
  .tree-emblem {
    position: absolute;
    border-radius: 48% 52% 40% 44% / 55% 55% 45% 45%;
  }
  .card-front .tree-emblem {
    left: 58px; top: 120px; width: 170px; height: 126px;
    background: var(--ink);
  }
  .ground-band {
    position: absolute; left: 0; right: 0; bottom: 0; height: 60px;
    background: var(--card-black);
  }
  .contact-list {
    position: absolute; left: 268px; top: 118px;
    border-left: 2px solid var(--ink);
    padding: 4px 0 4px 12px;
    list-style: none;
    font-family: "Lato", sans-serif; font-size: 14px;
    color: var(--text-grey);
  }
  .contact-item {
    display: flex; align-items: center; gap: 7px;
    height: 25px;
  }
  .contact-icon { width: 14px; height: 14px; flex: none; }
  .contact-dot {
    width: 11px; height: 11px; border-radius: 50%;
    background: var(--ink); flex: none; margin: 0 1.5px;
  }
  /* Back */
  .card-back { background: var(--card-black); }
  .card-back .tree-emblem {
    left: 188px; top: 78px; width: 164px; height: 120px;
    background: var(--emblem-grey);
  }
  .tagline {
    position: absolute; left: 0; right: 0; top: 212px;
    font-family: "Cinzel", serif; font-size: 13px;
    color: var(--tagline); text-align: center; letter-spacing: 0.3px;
    white-space: nowrap;
  }
</style>
</head>
<body>
<main class="canvas">
  <section class="card card-front">
    <h1 class="company-name">Silver Heron Holdings, LLC</h1>
    <div class="tree-emblem" role="img" aria-label="Black silhouette of a broad cypress tree"></div>
    <ul class="contact-list">
      <li class="contact-item">
        <svg class="contact-icon" viewBox="0 0 16 16" aria-hidden="true"><path fill="#111" d="M3.5 1.5l2.2 2.6-1.3 1.8c.9 2 2.6 3.8 4.7 4.8l1.8-1.3 2.6 2.2-1.4 2.4C6.7 13.6 2.3 9.2 1.1 3z"/></svg>
        555-014-2287
      </li>
      <li class="contact-item">
        <svg class="contact-icon" viewBox="0 0 16 16" aria-hidden="true"><rect x="1.5" y="3.5" width="13" height="9" fill="none" stroke="#111" stroke-width="1.4"/><path d="M1.5 3.5L8 9l6.5-5.5" fill="none" stroke="#111" stroke-width="1.4"/></svg>
        info@silverheronholdings.com
      </li>
      <li class="contact-item"><span class="contact-dot"></span>SilverHeronHoldingsGroup</li>
      <li class="contact-item"><span class="contact-dot"></span>@Silver_Heron</li>
    </ul>
    <div class="ground-band"></div>
  </section>

  <section class="card card-back">
    <div class="tree-emblem" role="img" aria-label="Light grey silhouette of a broad cypress tree"></div>
    <p class="tagline">STEADY ROOTS, LASTING GROWTH</p>
  </section>
</main>
</body>
</html>
```